Female Leadership Word/PDF template

I need a template, not just a design, for a word document in A4 size with a cover, middle pages and last page to give a nice as course material for a leadership training. I need it as a document to directly work in myself, to put in the text etc, ready to use , not just the design. I have attached 3 files. One that is an inspiration for how I like to have it (except the photos), one that is my style guide that shows the different elements to play with. I like it to be bright and stylish at the same time. I've added another document that shows some bright colors. My web page is www.brightpathgroup.se

Target Market(s)

Women leaders who like to perform but want to increase the soft and spiritual side in their lives and profession.

Industry/Entity Type

Leadership

Font styles to use
Sans Serif

Colors

Designer to choose colors to be used in the design.

Requirements
Must have
• Feel elegant, warm, welcoming and professional.
• Must be a document I can work in, not just a design that I should apply. Willing to pay more for that.
Should not have
• Dull. Hard.

```html
<!DOCTYPE html>
<html lang="en">
<head>
<meta charset="utf-8">
<title>Bright Path – Course Material Template</title>
<link href="https://fonts.googleapis.com/css2?family=Montserrat:wght@300;400;500;700;800&display=swap" rel="stylesheet">
<style>
  :root {
    --orange: #ec9535;
    --orange-soft: #f0a24c;
    --orange-glow: #f4b466;
    --taupe: #a39478;
    --ink: #6a6a6a;
    --white: #ffffff;
    --paper-light: #fbfbfb;
    --paper-shade: #e6e6e6;
    --page-edge: #c9c9c9;
  }
  * { margin: 0; padding: 0; box-sizing: border-box; }
  html, body { width: 1200px; height: 866px; overflow: hidden; background: var(--white); }
  body { position: relative; font-family: "Montserrat", sans-serif; }

  .page { position: absolute; top: 12px; width: 572px; height: 843px; border: 1px solid var(--page-edge); overflow: hidden; }

  /* Cover */
  .cover { left: 15px; }
  .cover-hero { position: absolute; left: 0; top: 0; width: 100%; height: 646px; background: var(--orange); }
  .cover-motif { position: absolute; left: -260px; top: 6px; width: 536px; height: 636px; border-radius: 50%;
    background: radial-gradient(circle, var(--orange-glow) 0%, var(--orange-soft) 45%, var(--orange) 72%); opacity: .75; }
  .cover-band { position: absolute; left: 0; top: 646px; width: 100%; height: 197px; background: var(--taupe); color: var(--white); text-align: right; padding: 22px 43px 0 0; }
  .cover-title { font-weight: 300; font-size: 24px; letter-spacing: .5px; line-height: 32px; }
  .cover-date { font-weight: 700; font-size: 23px; letter-spacing: .5px; line-height: 34px; }
  .brand { display: inline-flex; align-items: center; gap: 10px; color: var(--white); font-weight: 400; }
  .cover .brand { margin-top: 10px; font-size: 38px; letter-spacing: -.5px; }
  .brand-dot { border: 2px solid var(--white); border-radius: 50%; flex: none; }
  .cover .brand-dot { width: 68px; height: 68px; }

  /* Inner page */
  .inner { left: 613px; background: linear-gradient(90deg, var(--paper-shade) 0%, var(--paper-light) 55%, var(--paper-shade) 100%); }
  .inner-header { height: 52px; background: var(--orange-soft); display: flex; align-items: center; justify-content: space-between; padding: 0 14px 0 19px; }
  .inner-header h1 { color: var(--white); font-weight: 800; font-size: 22px; letter-spacing: 1px; }
  .inner-header .brand { font-size: 19px; gap: 7px; }
  .inner-header .brand-dot { width: 32px; height: 32px; border-width: 1.5px; }
  .inner-body { padding: 38px 30px 0 32px; color: var(--ink); font-size: 11.9px; line-height: 20.1px; }
  .inner-body p { margin-bottom: 20px; }
  .inner-body h2 { color: var(--orange); font-weight: 700; font-size: 16.5px; line-height: 20px; margin: 16px 0 2px; }
  .inner-body h2 + p { margin-bottom: 20px; }
  .inner-footer { position: absolute; left: 0; bottom: 0; width: 100%; height: 27px; background: var(--taupe); color: var(--white); font-size: 10.5px; letter-spacing: .5px; font-weight: 500; }
  .footer-copy { position: absolute; left: 10px; top: 8px; }
  .footer-page { position: absolute; right: 0; top: 0; height: 27px; width: 90px; background: var(--orange-soft); clip-path: polygon(20% 0, 100% 0, 100% 100%, 0 100%); text-align: right; padding: 8px 10px 0 0; }
</style>
</head>
<body>

<section class="page cover">
  <div class="cover-hero">
    <div class="cover-motif" role="img" aria-label="Large concentric decorative mandala pattern in pale orange"></div>
  </div>
  <div class="cover-band">
    <div class="cover-title">DOCUMENT TITLE HERE</div>
    <div class="cover-date">MARCH 2019</div>
    <div class="brand"><span class="brand-dot"></span>Bright Path</div>
  </div>
</section>

<section class="page inner">
  <header class="inner-header">
    <h1>EXECUTIVE SUMMARY</h1>
    <div class="brand"><span class="brand-dot"></span>Bright Path</div>
  </header>
  <main class="inner-body">
    <p>Lorem ipsum dolor sir Lorem ipsum dolor sirLorem ipsum dolor sirLorem ipsum dolor sirLorem ipsum dolor sirLorem ipsum dolor sirLorem ipsum dolor sirLorem ipsum dolor sirLorem ipsum dolor sir Lorem ipsum dolor sirLorem ipsum dolor sirLorem ipsum dolor sirLorem ipsum dolor sirLorem ipsum dolor sirLorem ipsum dolor sirLorem ipsum dolor sirLorem ipsum dolor sir Lorem ipsum dolor sirLorem ipsum dolor sirLorem ipsum dolor sirLorem ipsum dolor sirLorem ipsum dolor sirLorem ipsum dolor sirLorem ipsum dolor sirLorem ipsum dolor sir Lorem ipsum dolor sirLorem ipsum dolor sirLorem ipsum dolor sirLorem ipsum dolor sirLorem ipsum dolor sirLorem ipsum dolor sirLorem ipsum dolor sirLorem ipsum dolor sir Lorem ipsum dolor sirLorem ipsum dolor sirLorem ipsum dolor sirLorem ipsum dolor sirLorem ipsum dolor sirLorem ipsum dolor sirLorem ipsum dolor sirLorem ipsum dolor sir Lorem ipsum dolor sirLorem ipsum dolor sirLorem ipsum dolor sirLorem ipsum dolor sirLorem ipsum dolor</p>
    <h2>Paragraph Title here</h2>
    <p>sirLorem ipsum dolor sirLorem ipsum dolor sirLorem ipsum dolor sir Lorem ipsum dolor sirLorem ipsum dolor sirLorem ipsum dolor sirLorem ipsum dolor sirLorem ipsum dolor sirLorem ipsum dolor sirLorem ipsum dolor sirLorem ipsum dolor sir Lorem ipsum dolor sirLorem ipsum dolor sirLorem ipsum dolor sirLorem ipsum dolor sirLorem ipsum dolor sirLorem ipsum dolor sirLorem ipsum dolor sirLorem ipsum dolor sir Lorem ipsum dolor sirLorem ipsum dolor sirLorem ipsum dolor sirLorem ipsum dolor sirLorem ipsum dolor sirLorem ipsum dolor sirLorem ipsum dolor sirLorem ipsum dolor sir Lorem ipsum dolor sirLorem ipsum dolor sirLorem ipsum dolor sirLorem ipsum dolor sirLorem ipsum dolor sirLorem ipsum dolor sirLorem ipsum dolor sir</p>
    <p>sirLorem ipsum dolor sirLorem ipsum dolor sirLorem ipsum dolor sir Lorem ipsum dolor sirLorem ipsum dolor sirLorem ipsum dolor sirLorem ipsum dolor sirLorem ipsum dolor sirLorem ipsum dolor sirLorem ipsum dolor sirLorem ipsum dolor sir Lorem ipsum dolor sirLorem ipsum dolor sirLorem ipsum dolor sirLorem ipsum dolor sirLorem ipsum dolor sirLorem ipsum dolor sirLorem ipsum dolor sirLorem ipsum dolor sir Lorem ipsum dolor sirLorem ipsum dolor sirLorem ipsum dolor sirLorem ipsum dolor sirLorem ipsum dolor sirLorem ipsum dolor sirLorem ipsum dolor sir</p>
  </main>
  <footer class="inner-footer">
    <span class="footer-copy">COPYRIGHT TEXT HERE</span>
    <span class="footer-page">PAGE : 06</span>
  </footer>
</section>

</body>
</html>
```